Real Estate Development Sign

I am trying to get some good graphic design help for a new real estate development project. We need two designs for two separate large billboard-type directionals, also For Sale Signs, and also bandit directional signs. I have a company who have already given it a shot, but I don't like what they have come up with. I need it to have a WOW factor and pop to catch people's eye, but also simple and easy to read. I've attached what they have done so far. I have proofs of what has already been created and I've attached them. I've also attached the logo for the project, but I'm fine with changing the color for the logo to help make the overall signs more cohesive. I want clean, easy to read and eye catching. I will need to be able to pass the designs on to a company to have them printed for the billboards. One of them is 10x12 and the other is 8x10. Time is of the essence - I've spent too much time trying to get this other company to do what I want.
Updates

Project Deadline Extended
Reason: Need more submissions.

I would like to shoot for Black, Red, White and a touch of Yellow for the colors of the signs.

Industry/Entity Type

Graphic Design

```html
<!DOCTYPE html>
<html lang="en">
<head>
<meta charset="utf-8">
<title>Custom Garden Homes – Now Selling</title>
<link rel="stylesheet" href="https://fonts.googleapis.com/css2?family=Roboto:wght@500;700;900&family=Roboto+Condensed:wght@700&display=swap">
<style>
  :root {
    --board-white: #ffffff;
    --band-gold: #e8cd8c;
    --band-gold-deep: #d9b66a;
    --headline-red: #c8202a;
    --tag-green: #7fbf3a;
    --ink-brown: #3b2418;
    --logo-brown: #6b3a1f;
    --art-red: #d7262e;
    --art-gold: #e2b04a;
  }
  * { box-sizing: border-box; margin: 0; padding: 0; }
  html, body { width: 1200px; height: 934px; overflow: hidden; background: var(--board-white); }
  .billboard {
    position: relative;
    width: 1200px;
    height: 934px;
    background: var(--board-white);
    overflow: hidden;
    font-family: "Roboto", sans-serif;
  }
  .bands { position: absolute; inset: 0; }
  .headline {
    position: absolute;
    right: 40px;
    top: 38px;
    font-family: "Roboto", sans-serif;
    font-weight: 900;
    font-size: 82px;
    letter-spacing: 1px;
    color: var(--headline-red);
    transform: rotate(-3.5deg);
    transform-origin: right center;
  }
  .price-tag {
    position: absolute;
    left: 80px;
    top: 0;
    width: 320px;
    height: 380px;
  }
  .price-tag svg { position: absolute; inset: 0; }
  .price-tag__text {
    position: relative;
    padding-top: 118px;
    text-align: center;
    color: var(--board-white);
    font-family: "Roboto", sans-serif;
    font-weight: 700;
  }
  .price-tag__lead { font-size: 42px; line-height: 1; }
  .price-tag__amount { font-size: 92px; line-height: 1.05; font-weight: 900; }
  .product {
    position: absolute;
    left: 30px;
    top: 440px;
    width: 450px;
    text-align: center;
  }
  .product__title {
    font-family: "Roboto Condensed", sans-serif;
    font-weight: 700;
    font-size: 74px;
    line-height: 1.02;
    color: var(--ink-brown);
    text-transform: uppercase;
  }
  .product__builder {
    margin-top: 14px;
    font-family: "Roboto", sans-serif;
    font-weight: 500;
    font-size: 40px;
    color: var(--tag-green);
  }
  .hero-art {
    position: absolute;
    left: 500px;
    top: 220px;
    width: 680px;
    height: 500px;
    border-radius: 24px;
    background: radial-gradient(ellipse at 50% 45%, var(--art-red) 0%, #b51d24 45%, var(--art-gold) 80%, rgba(226,176,74,0) 100%);
  }
  .community-name {
    position: absolute;
    left: 60px;
    top: 790px;
    width: 370px;
    display: flex;
    align-items: center;
    gap: 14px;
    font-family: "Roboto", sans-serif;
    font-weight: 500;
    font-size: 38px;
    line-height: 1.05;
    color: var(--logo-brown);
  }
  .community-name__dot {
    flex: none;
    width: 22px; height: 22px;
    border-radius: 50%;
    background: var(--logo-brown);
  }
  .phone-arrow {
    position: absolute;
    left: 460px;
    top: 760px;
    width: 720px;
    height: 150px;
  }
  .phone-arrow svg.arrow-shape { position: absolute; inset: 0; }
  .phone-arrow__content {
    position: relative;
    height: 100%;
    display: flex;
    align-items: center;
    padding-left: 36px;
    gap: 22px;
  }
  .phone-arrow__number {
    font-family: "Roboto", sans-serif;
    font-weight: 700;
    font-size: 98px;
    color: var(--ink-brown);
    letter-spacing: -1px;
  }
</style>
</head>
<body>
  <div class="billboard">
    <svg class="bands" width="1200" height="934" viewBox="0 0 1200 934" aria-hidden="true">
      <polygon points="0,150 1200,20 1200,175 0,260" fill="var(--band-gold)"/>
      <polygon points="0,150 1200,20 1200,0 0,0" fill="var(--board-white)"/>
      <polygon points="0,720 1200,690 1200,934 0,934" fill="var(--band-gold)"/>
      <polygon points="0,720 1200,690 1200,702 0,732" fill="var(--band-gold-deep)"/>
    </svg>

    <div class="headline">NOW SELLING</div>

    <div class="price-tag">
      <svg width="320" height="380" viewBox="0 0 320 380" aria-hidden="true">
        <polygon points="0,0 320,0 320,340 160,380 0,340" fill="var(--tag-green)"/>
      </svg>
      <div class="price-tag__text">
        <div class="price-tag__lead">From the low</div>
        <div class="price-tag__amount">$200’s</div>
      </div>
    </div>

    <div class="product">
      <div class="product__title">Custom<br>Garden Homes</div>
      <div class="product__builder">by Brannock Homes</div>
    </div>

    <div class="hero-art" role="img" aria-label="Illustration of a red house rising out of an open gift box tied with gold ribbons"></div>

    <div class="community-name">
      <span class="community-name__dot"></span>
      <span>The Grove at Summit Ridge</span>
    </div>

    <div class="phone-arrow">
      <svg class="arrow-shape" width="720" height="150" viewBox="0 0 720 150" aria-hidden="true">
        <polygon points="0,0 640,0 720,75 640,150 0,150" fill="var(--board-white)"/>
      </svg>
      <div class="phone-arrow__content">
        <svg width="64" height="64" viewBox="0 0 64 64" aria-label="Phone" role="img">
          <circle cx="32" cy="32" r="29" fill="none" stroke="var(--ink-brown)" stroke-width="4"/>
          <path d="M22 18c2-2 5-2 6 1l3 6c1 2 0 3-1 4l-2 2c2 4 5 7 9 9l2-2c1-1 3-2 4-1l6 3c3 1 3 4 1 6l-3 3c-3 3-11 0-18-7s-10-15-7-18z" fill="var(--ink-brown)"/>
        </svg>
        <span class="phone-arrow__number">512.555.0148</span>
      </div>
    </div>
  </div>
</body>
</html>
```